Five steps to on-time delivery

We need a SIMPLE and EFFECTIVE one-pager to help get our customers to do what we need to help them.
We are a contract packing business.
Our customers send us their product for us to pack.
Eg. Customer sends us 20 tonne of nuts, we run through our production lines to make 150g bags (of nuts) you buy from the supermarket.
We are driven mad because our customers constantly ask us to pack things before we've got them - or the minute after we've received the last component.
We run with 100+ people, 3 shifts on a 20,000sq meter site. we handle 1,000's of transactions a day. We need to be in control. This starts with our customers understanding it takes time to plan, order, schedule, set up, start, run, etc.
This would certainly be part of a Starter Pack (Contact details, Delivery Standards, Account Application, etc) and then no doubt sent out again and again to repeat offenders.
I will attach an excel file (if i can) that indicates the sort of thing i'm after. Sheet 1 (5) is the closest i've got. other sheets show the 'journey' but discarded because too 'busy'. Has to be simple/engaging/effective.
I've been bold and had a pathetic go at being creative with the blurb down the side of the page. Otherwise i felt our audience would fall asleep (it's a pretty dry topic - and our customers don't want to be told what to do by one of their suppliers). I'm hoping you get the idea of what i was trying to do - over to you for the creative part.
ps. have also uploaded examples of stationery and PACKWELL Delivery Standards - that we've been sending out to Customers for years (and they don't pay any attention).
Reason: have extended deadline due to files not uploading yesterday.
Procurement people. Operations. Manufacturers. Large and small. Mainly in food industry.
Business

```html
<!DOCTYPE html>
<html lang="en">
<head>
<meta charset="utf-8">
<title>5 Steps to On-Time Delivery</title>
<link rel="stylesheet" href="https://fonts.googleapis.com/css2?family=Inter:ital,wght@0,300;0,400;0,700;1,300&display=swap">
<style>
  :root {
    --brand-red: #e4412f;
    --brand-navy: #1f3370;
    --ink: #231f20;
    --paper: #ffffff;
  }
  * { box-sizing: border-box; margin: 0; padding: 0; }
  html, body { width: 1200px; height: 900px; overflow: hidden; background: var(--paper); }
  body { font-family: "Inter", Helvetica, Arial, sans-serif; color: var(--ink); position: relative; }

  .brand-mark {
    position: absolute; left: 972px; top: 90px; width: 176px; height: 90px;
    background: var(--brand-red); color: var(--paper);
    display: flex; align-items: center; justify-content: center;
    font-weight: 700; font-size: 16px; letter-spacing: 0.2px;
  }

  .page-title {
    position: absolute; left: 54px; top: 180px;
    font-weight: 300; font-size: 35px; color: var(--brand-red); letter-spacing: 0.3px;
  }

  .intro {
    position: absolute; left: 55px; top: 236px; width: 540px;
    font-size: 14.3px; line-height: 21.3px; font-weight: 400;
  }

  .steps {
    position: absolute; left: 53px; top: 385px; width: 1099px; height: 387px;
    display: flex;
  }
  .step {
    --accent: var(--brand-red);
    flex: 1; position: relative;
    border: 3px solid var(--accent); border-bottom-width: 6px; border-top: 0;
    background: var(--paper);
  }
  .step--final { --accent: var(--brand-navy); }

  .step__head {
    height: 125px; background: var(--accent); color: var(--paper);
    position: relative; margin: 0 -3px; padding-left: 4px;
  }
  .step__number {
    position: absolute; left: 3px; top: 4px;
    font-weight: 300; font-size: 62px; line-height: 62px;
  }
  .step__name {
    position: absolute; left: 42px; top: 28px;
    font-weight: 300; font-size: 25px; line-height: 25px; text-transform: uppercase;
  }
  .step__name--two-line { top: 16px; left: 52px; }
  .step__name--wide { left: 50px; }

  .step__lead {
    position: absolute; left: 9px; right: 9px; top: 76px; height: 37px;
    background: var(--paper); color: var(--brand-navy);
    font-weight: 700; font-size: 13.5px; line-height: 13.5px;
    padding: 5px 0 0 26px; text-transform: uppercase;
  }

  .step__pointer { position: absolute; left: -1px; top: 125px; width: 70px; height: 40px; }
  .step__pointer polygon { fill: var(--accent); }

  .step__list {
    list-style: none; position: absolute; top: 180px; left: 30px; right: 10px;
    font-weight: 300; font-size: 17.5px; line-height: 20px; text-transform: uppercase;
  }
  .step__list li + li { margin-top: 20px; }
  .step__list--tight li + li { margin-top: 16px; }
  .lead-time { font-style: italic; font-size: 11px; text-transform: uppercase; margin-left: 22px; }
  .lead-time--inline { margin-left: 4px; }
</style>
</head>
<body>

<div class="brand-mark">PACKWELL LOGO HERE</div>

<h1 class="page-title">5 STEPS TO ON-TIME DELIVERY</h1>

<p class="intro">In commitment to customer satisfaction and affordable pricing please follow the step by step guidelines below for an on-time delivery of your product. If you have any questions please contact your Packwell representative or to find more information on our delivery process visit our website www.packwell.net.au.</p>

<section class="steps">
  <article class="step">
    <div class="step__head">
      <span class="step__number">1</span>
      <h2 class="step__name">Forecasts</h2>
      <p class="step__lead">Required at least<br>4-12 weeks prior</p>
    </div>
    <svg class="step__pointer" viewBox="0 0 70 40" aria-hidden="true"><polygon points="0,0 70,0 35,40"/></svg>
    <ul class="step__list">
      <li>Capacity<br>Planning <span class="lead-time">6-12 mo.</span></li>
      <li>Purchasing <span class="lead-time lead-time--inline">3 mo.</span></li>
    </ul>
  </article>

  <article class="step">
    <div class="step__head">
      <span class="step__number">2</span>
      <h2 class="step__name step__name--wide">New Jobs</h2>
      <p class="step__lead">Required at least<br>4-12 weeks prior</p>
    </div>
    <svg class="step__pointer" viewBox="0 0 70 40" aria-hidden="true"><polygon points="0,0 70,0 35,40"/></svg>
    <ul class="step__list">
      <li>Trials</li>
      <li>Material<br>Specification</li>
      <li>Packing<br>Instructions</li>
      <li>Pricing</li>
    </ul>
  </article>

  <article class="step">
    <div class="step__head">
      <span class="step__number">3</span>
      <h2 class="step__name step__name--two-line">Purchase<br>Orders</h2>
      <p class="step__lead">Required at least<br>1 week prior</p>
    </div>
    <svg class="step__pointer" viewBox="0 0 70 40" aria-hidden="true"><polygon points="0,0 70,0 35,40"/></svg>
    <ul class="step__list step__list--tight">
      <li>Part(s)</li>
      <li>Quantities</li>
      <li>Prices</li>
      <li>Delivery Dates</li>
    </ul>
  </article>

  <article class="step">
    <div class="step__head">
      <span class="step__number">4</span>
      <h2 class="step__name step__name--wide">Materials</h2>
      <p class="step__lead">Required at least<br>1 week prior</p>
    </div>
    <svg class="step__pointer" viewBox="0 0 70 40" aria-hidden="true"><polygon points="0,0 70,0 35,40"/></svg>
    <ul class="step__list">
      <li>All materials<br>received in full</li>
      <li>Agreed<br>specification</li>
      <li>Compliant with<br>Packwell delivery<br>standards</li>
    </ul>
  </article>

  <article class="step step--final">
    <div class="step__head">
      <span class="step__number">5</span>
      <h2 class="step__name step__name--wide">Priorities</h2>
      <p class="step__lead">Required at least<br>1 week prior</p>
    </div>
    <svg class="step__pointer" viewBox="0 0 70 40" aria-hidden="true"><polygon points="0,0 70,0 35,40"/></svg>
    <ul class="step__list">
      <li>Priorities and<br>materials<br>managed in<br>weekly buckets<br>within the<br>month</li>
    </ul>
  </article>
</section>

</body>
</html>
```